Church needs a graphic design/flyer layout for upcoming series

I need a multi-purpose design for promoting both our upcoming series of messages and our fall kick-off event where we will launch the messages.

Our promotion will be printed on a two-sided. One side is simple and focuses on the series and the other side has details in regards to the event. I have provided an attachment example of what we did last time.

The design needs to be multi-purpose because it will be used for our sermon Power Points, placed on our website banner, social media, etc.

• Sermon series is called “Quiet Questions”
• The subtitle will be “What’s keeping you from God?”
• Our name logo should be on the graphic as well.
• The subject manner will revolve around common hurdles that people face about God and Christianity: The existence of God, the exclusivity of religion, Hell, the reliability of the Bible, Hypocrisy in the church, etc.
• Our mission is “Connecting Young Families to Christ” so our focus is to reach out to families while not being exclusive to others.
• Our target audience is families with school-aged kids.
• This series is an invitational focus so we want it to be appealing to non-church goers.
• It should be attention grabbing while not being too ‘edgy’

• The front of the card will most likely consist the Sermon Series Graphic, title & subtitle of the series, and perhaps our name logo somewhere on it.
• The back of the card will invite and give the basic information for the event so that the people will be encouraged to save the date and come to the event.
• Here are some things that could be included on that advertisement:
o The name of the event: “Harbor Church Fall Kick-off”
o The date and time of the event: Sept 23rd @ 10:30
o Features of the event:
 Free lunch
 Children’s program
 Bouncy Castle
 Start of the “Quiet Questions” messages.
 Sample of topics
o Information about the church: our website and address, etc
o Engaging pictures and graphics.
• The rest of the tone and manner are the same as the sermon series graphic.
The flyer will be 11X14, like a postcard size.

Target Market(s)

Young families who are spiritually curious but not committed church attenders.

Colors

Designer to choose colors to be used in the design.

Requirements
Nice to have
• A modern and professional looking design.
Should not have
• Anything offensive or not family friendly.

```html
<!DOCTYPE html>
<html lang="en">
<head>
<meta charset="utf-8">
<title>Quiet Questions – Harbor Church Fall Kick-off</title>
<link rel="stylesheet" href="https://fonts.googleapis.com/css2?family=Open+Sans:ital,wght@0,400;0,700;1,400&family=Cabin:wght@500;600&family=Comfortaa:wght@500&family=Oswald:wght@300;500&display=swap">
<style>
:root{
  --page:#ffffff;
  --sea:#a9d6dc;
  --foam:#eef5f2;
  --sand:#c9b9a2;
  --sand-dark:#9e8e78;
  --brown:#6e5535;
  --brown-deep:#4e3b22;
  --orange:#f58a1f;
  --white:#ffffff;
  --ink:#2b2b2b;
  --gold:#b9aa7a;
  --gold-light:#d8cca3;
  --sky:#4d86c9;
  --grass:#6aa84f;
  --band-text:#4e3b22;
}
*{margin:0;padding:0;box-sizing:border-box}
html,body{width:915px;height:1200px;overflow:hidden;background:var(--page)}
.sheet{position:relative;width:915px;height:1200px}
.card{position:absolute;left:85px;width:744px;height:584px;overflow:hidden;border:1px solid #222}
.card--front{top:8px}
.card--back{top:608px;background:var(--brown)}

/* front */
.beach-photo{position:absolute;inset:0;
  background:linear-gradient(165deg,var(--sea) 0%,var(--foam) 22%,#e8ddc9 32%,var(--sand) 55%,var(--sand-dark) 100%)}
.brand{position:absolute;display:flex;align-items:center;gap:10px;font-family:"Oswald",sans-serif;font-weight:300;color:var(--ink);white-space:nowrap}
.brand__dot{width:26px;height:26px;border-radius:50%;background:var(--orange)}
.card--front .brand{left:14px;top:142px;font-size:27px}
.series-name{position:absolute;right:28px;top:190px;font-family:"Oswald",sans-serif;font-weight:500;font-size:34px;letter-spacing:3px;text-transform:uppercase;color:var(--brown-deep)}
.series-oval{position:absolute;left:112px;top:253px;width:518px;height:314px;border-radius:50%;background:rgba(255,255,255,.28)}
.series-title{position:absolute;left:0;width:100%;text-align:center;font-family:"Open Sans",sans-serif;font-weight:700;color:var(--white);line-height:1}
.series-title--1{top:290px;font-size:56px}
.series-title--2{top:388px;font-size:42px}
.series-title--3{top:474px;font-size:56px}

/* back */
.event-name{position:absolute;top:12px;left:0;width:100%;text-align:center;font-family:"Cabin",sans-serif;font-weight:600;font-size:56px;color:var(--white);white-space:nowrap}
.save-badge{position:absolute;left:33px;top:93px;width:80px;height:80px;border:3px solid var(--orange);border-radius:50%}
.event-date{position:absolute;left:145px;top:116px;font-family:"Cabin",sans-serif;font-weight:500;font-size:28px;color:var(--orange)}
.features-heading{position:absolute;right:26px;top:174px;font-family:"Open Sans",sans-serif;font-style:italic;font-weight:400;font-size:42px;color:var(--white);text-decoration:underline;text-decoration-thickness:2px;text-underline-offset:6px;white-space:nowrap}
.features{position:absolute;left:289px;top:242px;list-style:none;font-family:"Comfortaa",sans-serif;font-size:16.5px;color:var(--white);line-height:24.6px}
.features li::before{content:"• ";font-size:12px}
.hex{position:absolute;clip-path:polygon(25% 0,75% 0,100% 50%,75% 100%,25% 100%,0 50%)}
.hex--ring{background:var(--white)}
.hex--collage{left:93px;top:286px;width:166px;height:112px;background:linear-gradient(135deg,#cfc6b4,#6d6a6c 55%,#8c8070)}
.hex--building{left:11px;top:376px;width:164px;height:113px;background:linear-gradient(180deg,var(--sky) 0%,#9cc3e8 50%,var(--grass) 70%,#b5b5b5 100%)}
.hex--mission{left:179px;top:376px;width:164px;height:113px;background:radial-gradient(circle,var(--gold-light),var(--gold));display:flex;align-items:center;justify-content:center;text-align:center;font-family:"Oswald",sans-serif;font-weight:300;font-size:20px;line-height:26px;color:#5d5236}
.card--back .brand{right:24px;top:468px;font-size:20px;color:#2f2518}
.card--back .brand__dot{width:22px;height:22px}
.contact-band{position:absolute;left:0;top:507px;width:100%;height:68px;background:var(--white);
  clip-path:polygon(2% 8%,20% 0,50% 6%,80% 0,100% 10%,97% 50%,100% 92%,70% 100%,40% 94%,12% 100%,0 88%,4% 50%);
  text-align:center;font-family:"Cabin",sans-serif;font-weight:500;font-size:13px;color:var(--band-text);padding-top:12px;line-height:23px}
.icon{display:inline-block;width:9px;height:9px;border-radius:50%;background:var(--band-text);margin-right:4px;vertical-align:-1px}
</style>
</head>
<body>
<main class="sheet">
  <section class="card card--front">
    <div class="beach-photo" role="img" aria-label="Footprints in beach sand leading away from the surf, with a small cross standing in the sand"></div>
    <div class="brand"><span class="brand__dot"></span>Cedar Bay Harbor Church</div>
    <p class="series-name">Quiet Questions</p>
    <div class="series-oval"></div>
    <p class="series-title series-title--1">“WHAT’S</p>
    <p class="series-title series-title--2">KEEPING YOU FROM</p>
    <p class="series-title series-title--3">GOD?”</p>
  </section>

  <section class="card card--back">
    <h1 class="event-name">“Harbor Church Fall Kick-off”</h1>
    <div class="save-badge"></div>
    <p class="event-date">September 23rd @ 10:30</p>
    <h2 class="features-heading">Features of the event ...</h2>
    <ul class="features">
      <li>Free lunch</li>
      <li>Children’s program</li>
      <li>Bouncy Castle</li>
      <li>Start of the “Quiet Questions” messages.</li>
      <li>Sample of topics</li>
    </ul>
    <div class="hex hex--ring" style="left:89px;top:282px;width:174px;height:120px"></div>
    <div class="hex hex--collage" role="img" aria-label="Collage of church life photos: a speaker with a book and gathered families"></div>
    <div class="hex hex--ring" style="left:7px;top:372px;width:172px;height:121px"></div>
    <div class="hex hex--building" role="img" aria-label="Church building with lawn and trees under a blue sky"></div>
    <div class="hex hex--ring" style="left:175px;top:372px;width:172px;height:121px"></div>
    <div class="hex hex--mission">Connecting<br>Young Families<br>to Christ</div>
    <div class="brand"><span class="brand__dot"></span>Cedar Bay Harbor Church</div>
    <div class="contact-band">
      <span class="icon"></span>118 Lantern Row, Brookfield, ON K0A 2B3, Canada<br>
      <span class="icon"></span>555 201 4480 &nbsp;|&nbsp; <span class="icon"></span>hello@cedarbayharbor.org &nbsp;|&nbsp; <span class="icon"></span>www.cedarbayharbor.org
    </div>
  </section>
</main>
</body>
</html>
```